Business Card + Letterhead Design for KESTOVA TRADING INC.

We already have a logo; now we need a business card + letterhead. We import and distribute flags and souvenirs with an emphasis on soccer related memorabilia. We target various ethnic markets and sporting goods stores. "International Souvenirs"

```html
<!DOCTYPE html>
<html lang="en">
<head>
<meta charset="utf-8">
<title>Kestova Trading – Letterhead &amp; Business Cards</title>
<link href="https://fonts.googleapis.com/css2?family=Arimo:wght@400;700&display=swap" rel="stylesheet">
<style>
  :root {
    --backdrop: #1c1c1c;
    --paper: #ffffff;
    --brand-red: #6e0000;
    --brand-red-light: #8a0c0c;
    --brand-red-dark: #560000;
    --rule-red: #9a3a3a;
    --watermark: rgba(110, 0, 0, 0.07);
    --card-watermark: rgba(255, 255, 255, 0.08);
    --ink-white: #ffffff;
    --ink-dark: #3a0000;
  }
  * { margin: 0; padding: 0; box-sizing: border-box; }
  html, body { width: 1200px; height: 971px; overflow: hidden; }
  body {
    background: var(--backdrop);
    font-family: "Arimo", Arial, sans-serif;
    position: relative;
  }

  /* Letterhead */
  .letterhead {
    position: absolute; left: 51px; top: 104px;
    width: 532px; height: 751px;
    background: var(--paper);
    box-shadow: 0 4px 18px rgba(0,0,0,.5);
    overflow: hidden;
  }
  .letterhead .tab {
    position: absolute; left: 32px; top: 0;
    width: 90px; height: 84px;
    background: var(--brand-red);
    border-radius: 0 0 8px 8px;
  }
  .letterhead .header-rule {
    position: absolute; left: 122px; right: 0; height: 1px;
    background: linear-gradient(to right, var(--rule-red), rgba(154,58,58,0));
  }
  .letterhead .header-rule.top { top: 13px; }
  .letterhead .header-rule.bottom { top: 71px; }
  .letterhead .brand-name {
    position: absolute; left: 132px; top: 30px;
    font-size: 20px; font-weight: 700; letter-spacing: 1px;
    white-space: nowrap;
    color: var(--brand-red);
  }
  .letterhead .watermark {
    position: absolute; left: 40px; top: 300px;
    width: 260px; height: 260px; border-radius: 50%;
    background: var(--watermark);
  }
  .letterhead .footer-rule {
    position: absolute; left: 0; right: 0; top: 723px; height: 2px;
    background: var(--brand-red);
  }
  .letterhead .address {
    position: absolute; left: 0; right: 0; top: 732px;
    text-align: center; font-size: 11px; color: var(--ink-dark);
  }

  /* Business cards */
  .card {
    position: absolute; left: 653px;
    width: 443px; height: 273px;
    border-radius: 12px;
    background: linear-gradient(135deg, var(--brand-red-light), var(--brand-red) 50%, var(--brand-red-dark));
    box-shadow: 0 4px 18px rgba(0,0,0,.5);
    overflow: hidden;
  }
  .card.front { top: 237px; }
  .card.back { top: 540px; }
  .card .panel {
    position: absolute; top: 0;
    background: var(--paper);
  }
  .card.front .panel { left: 21px; width: 168px; height: 159px; border-radius: 0 0 12px 12px; }
  .card.back .panel {
    left: 18px; width: 166px; height: 157px; border-radius: 0 0 12px 12px;
    display: flex; align-items: center; justify-content: center;
    padding: 0 10px;
  }
  .card .panel-mark {
    position: absolute; left: 50%; top: 50%;
    width: 70px; height: 70px; margin: -35px 0 0 -35px;
    border-radius: 50%; background: var(--brand-red);
  }
  .card .watermark {
    position: absolute; right: 20px; top: 60px;
    width: 200px; height: 200px; border-radius: 50%;
    background: var(--card-watermark);
  }
  .card .rule {
    position: absolute; right: 0; height: 1px;
    background: linear-gradient(to right, rgba(255,255,255,.85), rgba(255,255,255,.2));
  }
  .card.front .rule { left: 193px; }
  .card.front .rule.upper { top: 163px; }
  .card.front .rule.lower { top: 230px; }
  .card.front .brand-name {
    position: absolute; left: 198px; top: 184px;
    font-size: 21px; font-weight: 700; letter-spacing: 1px;
    white-space: nowrap;
    color: var(--ink-white);
  }
  .card.back .brand-name {
    font-size: 14px; font-weight: 700; letter-spacing: .5px;
    white-space: nowrap;
    color: var(--brand-red);
  }
  .card.back .person-name {
    position: absolute; left: 215px; top: 57px;
    font-size: 24px; white-space: nowrap;
    color: var(--ink-white);
  }
  .card.back .rule { left: 190px; }
  .card.back .rule.upper { top: 160px; }
  .card.back .rule.lower { top: 243px; }
  .card.back .contact {
    position: absolute; left: 190px; top: 166px;
    list-style: none; font-size: 14px; line-height: 18px;
    white-space: nowrap;
    color: var(--ink-white);
  }
</style>
</head>
<body>

  <section class="letterhead" aria-label="Letterhead">
    <div class="tab"></div>
    <div class="header-rule top"></div>
    <div class="header-rule bottom"></div>
    <div class="brand-name">KESTOVA TRADING</div>
    <div class="watermark"></div>
    <div class="footer-rule"></div>
    <p class="address">220-48 Harlow Ave. Toronto, ON, Canada M4B2K7</p>
  </section>

  <section class="card front" aria-label="Business card front">
    <div class="panel"><div class="panel-mark"></div></div>
    <div class="watermark"></div>
    <div class="rule upper"></div>
    <div class="brand-name">KESTOVA TRADING</div>
    <div class="rule lower"></div>
  </section>

  <section class="card back" aria-label="Business card back">
    <div class="panel"><span class="brand-name">KESTOVA TRADING</span></div>
    <div class="watermark"></div>
    <p class="person-name">Daniel Moreau</p>
    <div class="rule upper"></div>
    <ul class="contact">
      <li>Phone: (647) 555-0148</li>
      <li>Fax: (866) 555-0192</li>
      <li>Email: sales@kestovatrading.ca</li>
      <li>Web:kestovatrading.ca</li>
    </ul>
    <div class="rule lower"></div>
  </section>

</body>
</html>
```